Business Card Design - Construction Company

Tarrowin Construction is in need of a sharp, modern business card design that has an architectural/high fashion feel.

We are looking for a two sided card.

One side simple dark grey/black with some texture in the background. e.g. (a mosaic of simple interconnecting shapes or a shadow of the logo.) Something to draw attention and create interest.It will need to feature a large Tarrowin construction logo (files attached) in metallic gradient or plain white.

The other side should contain all of our information:

(in largest text)
Name of person
Tarrowin Construction Pty. Ltd.

Licensed builders specialising in:
- Bathrooms
- Kitchens
- Commercial interiors

(mid sized text)
Phone number
Fax number
person@tarrowinconstruction.example.au
www. tarrowinconstruction.example.au

(smaller text)
ABN: 62407938215
BSA license: xxx-xxxx
PO Box 8641 Kellsmoor QLD 4019 (address)

Target Market(s)

professional home and business owners

Industry/Entity Type

Construction

Requirements
Must have
• Must be bold, professional looking and modern.
Nice to have
• We are undecided as to what kind of printing we will go with.
Definitely square edged.
Probably high quality satin card.
We are also interested in designs that would work well on transparent or translucent plastic.
Ideally we would print two versions.
Should not have
• Nothing with an antique feel.
No wild colours. Small amounts of colour can be good in the right place.

```html
<!DOCTYPE html>
<html lang="en">
<head>
<meta charset="utf-8">
<title>Business Card Design – Tarrowin Construction</title>
<link rel="stylesheet" href="https://fonts.googleapis.com/css2?family=Encode+Sans+Condensed:wght@300;400&family=Roboto+Condensed:wght@400;700&family=Arimo:wght@400;700&display=swap">
<style>
  :root {
    --board-light: #f4f4f4;
    --board-mid: #dcdcdc;
    --board-dark: #c9c9c9;
    --card-black: #1f1d1c;
    --card-charcoal: #2b2928;
    --brand-blue: #1f5fae;
    --brand-blue-dark: #0f3f82;
    --accent-sky: #7fb8e6;
    --text-white: #ffffff;
    --text-soft: #8b8886;
    --metal: #b9b9b9;
    --title-slate: #4a5170;
    --title-ink: #2a2a2a;
    --rule: #a9a9a9;
    --label-grey: #8a8a8a;
  }
  * { margin: 0; padding: 0; box-sizing: border-box; }
  html, body { width: 1200px; height: 846px; overflow: hidden; }
  body {
    position: relative;
    background: radial-gradient(ellipse at 30% 30%, var(--board-light) 0%, var(--board-mid) 65%, var(--board-dark) 100%);
    font-family: "Arimo", Arial, sans-serif;
  }
  .card {
    position: absolute;
    left: 169px;
    width: 508px;
    height: 291px;
    background: linear-gradient(160deg, var(--card-charcoal) 0%, var(--card-black) 60%);
    box-shadow: 2px 4px 8px rgba(0,0,0,0.45);
    overflow: hidden;
  }
  .card--front { top: 105px; }
  .card--back { top: 460px; height: 290px; }

  .name-band {
    position: absolute;
    left: 42px; top: 0;
    width: 224px; height: 90px;
    background: linear-gradient(180deg, #3479c9 0%, var(--brand-blue) 45%, var(--brand-blue-dark) 100%);
    color: var(--text-white);
    padding: 40px 0 0 16px;
  }
  .name-band__company {
    font-family: "Arimo", Arial, sans-serif;
    font-weight: 700;
    font-size: 15px;
    letter-spacing: 1.2px;
    line-height: 1;
  }
  .name-band__entity {
    font-size: 9.5px;
    letter-spacing: 1.4px;
    margin-top: 7px;
    font-weight: 700;
  }
  .services {
    position: absolute;
    left: 279px; top: 26px;
    font-family: "Roboto Condensed", Arial, sans-serif;
    font-size: 12px;
    line-height: 16px;
  }
  .services__lead { color: var(--text-white); font-weight: 700; }
  .services__item { color: var(--accent-sky); }

  .person {
    position: absolute;
    left: 56px; top: 160px;
    color: var(--text-white);
  }
  .person__name {
    font-family: "Roboto Condensed", Arial, sans-serif;
    font-weight: 700;
    font-size: 24px;
    line-height: 1;
    margin-bottom: 12px;
  }
  .contact {
    list-style: none;
    font-size: 11px;
    line-height: 17px;
  }
  .legal {
    position: absolute;
    right: 28px; top: 220px;
    text-align: right;
    color: var(--text-soft);
    font-size: 8px;
    line-height: 15px;
  }

  .back-texture {
    position: absolute;
    inset: 0;
    background: linear-gradient(160deg, #2d2b2a 0%, #232120 100%);
  }
  .brand-lockup {
    position: absolute;
    left: 0; right: 0; top: 70px;
    text-align: center;
    color: var(--metal);
    font-family: "Arimo", Arial, sans-serif;
    font-weight: 700;
  }
  .brand-lockup__dot {
    display: block;
    width: 60px; height: 60px;
    margin: 0 auto 20px;
    border-radius: 50%;
    background: var(--metal);
  }
  .brand-lockup__name {
    font-size: 20px;
    letter-spacing: 1.5px;
    line-height: 1.3;
  }

  .presentation { position: absolute; left: 764px; top: 113px; width: 318px; }
  .presentation__rule { height: 2px; background: var(--rule); }
  .presentation__kicker {
    font-family: "Encode Sans Condensed", sans-serif;
    font-weight: 400;
    color: var(--title-slate);
    font-size: 29px;
    margin: 15px 0 0 5px;
    line-height: 1;
  }
  .presentation__kicker small { font-size: 18px; margin-left: 4px; }
  .presentation__client {
    font-family: "Encode Sans Condensed", sans-serif;
    font-weight: 300;
    color: var(--title-ink);
    font-size: 40px;
    margin: 8px 0 14px 4px;
    line-height: 1.1;
    white-space: nowrap;
  }
  .variant-label {
    position: absolute;
    left: 768px; top: 712px;
    font-family: "Encode Sans Condensed", sans-serif;
    font-weight: 300;
    font-size: 40px;
    color: var(--label-grey);
  }
</style>
</head>
<body>
  <section class="card card--front" aria-label="Card front">
    <div class="name-band">
      <div class="name-band__company">TARROWIN</div>
      <div class="name-band__entity">CONSTRUCTION PTY. LTD.</div>
    </div>
    <div class="services">
      <div class="services__lead">Licensed builders specialising in:</div>
      <div class="services__item">- Bathrooms</div>
      <div class="services__item">- Kitchens</div>
      <div class="services__item">- Commercial interiors</div>
    </div>
    <div class="person">
      <div class="person__name">John Doe</div>
      <ul class="contact">
        <li>{P}&nbsp; 0400 5550 12</li>
        <li>{F}&nbsp; 0755 5019 37</li>
        <li>{E}&nbsp; person@tarrowinconstruction.example.au</li>
        <li>{W}&nbsp; www. tarrowinconstruction.example.au</li>
      </ul>
    </div>
    <div class="legal">
      <div>ABN: 62407938215</div>
      <div>BSA license: xxx-xxxx</div>
      <div>PO Box 8641 Kellsmoor QLD 4019</div>
    </div>
  </section>

  <section class="card card--back" aria-label="Card back">
    <div class="back-texture" role="img" aria-label="Dark repeating brand-mark pattern texture"></div>
    <div class="brand-lockup">
      <span class="brand-lockup__dot"></span>
      <div class="brand-lockup__name">TARROWIN CONSTRUCTION</div>
    </div>
  </section>

  <header class="presentation">
    <div class="presentation__rule"></div>
    <p class="presentation__kicker">Business Card Design <small>for</small></p>
    <h1 class="presentation__client">Tarrowin Construction</h1>
    <div class="presentation__rule"></div>
  </header>

  <p class="variant-label">Type B - ii</p>
</body>
</html>
```